High-end Oceanfront Real Estate Group Needs Clean, Modern Web Design

I’m looking for a clean, professional, modern and beautiful homepage web design for a Real Estate group in Southern California, USA.

The group/company is “Marlow on the Shore,” and they specialize in high end (i.e. expensive), oceanfront real estate in the Orange County area.

The look and feel of the page should accentuate the brand qualities: luxurious/expensive, professional, and beautiful (Orange County is one of the most beautiful areas in all the US and we would love the site to emphasize the beautiful beaches and scenery it has to offer).

Looks we like:
• www.brantleyhomesrealty.example
• www.keptbyfenwick.example -- I think the design is pretty out-dated in this site, but I like the organization/layout of the site

Header Tags (I don’t know if we can fit all of these, may need a side-menu, but I’d prefer header title only if possible):
• Welcome
• Featured Listings
• Previously Sold
• Sell
• Property Search
• Team
• Videos
• Blog
• Explore O.C.
• Contact

I have attached the beach and logo pics that we would like to use as the header, a few pictures of the team, and one sample home/view pic which can be used in any of the other sections (for pictures of the homes, just find expensive oceanfront houses and that will be fine).

I promise to provide feedback to each and every design submission. I appreciate the hard work that all of you are putting into your designs. There can be only one contest winner, but I hope to give all of you helpful feedback to submit the best designs possible!

Target Market(s)

Very wealthy home owners of oceanfront properties. These properties are worth several millions of dollars, and thus the site and brand needs to be targeted to very wealthy, successful individuals and families (both US and international buyers).

Industry/Entity Type

Real Estate

Number of Pages Required

2 page

Requirements
Must have
• I don’t want to give too many requirements, because I want to let you all be creative. However, here are the few Must Haves:
• Must submit 2 page designs (a home page and a sub page)
• Must use logo provided
• Focus is mostly on homes, but I would like to include some beach/ocean imagery as well
• The first “item” on the home page should be an accordion/slider which shows pictures of homes and with 1 line of text: “List with the Leader” and two link buttons: “Sell Your Home” and “Buy Your Home”
• Color palette needs to be mainly blues--to match ocean and sky blue
• Exported in all major formats (psd,ai,eps,png,jpeg,etc)
Nice to have
• We don’t necessarily need all of these, but would like to feature most:
• List of videos
• “Meet the Team”—brief team bios and pics
• Link(s) to Blog
• “List with the Leader” – section on why they should choose this firm
• Featured Listings
• Previously Sold

```html
<!DOCTYPE html>
<html lang="en">
<head>
<meta charset="utf-8">
<title>Marlow on the Shore — Homepage</title>
<link rel="stylesheet" href="https://fonts.googleapis.com/css2?family=Josefin+Sans:wght@400;600;700&display=swap">
<style>
  :root {
    --header-bg: #3b3b3d;
    --strip-bg: #3a3a3c;
    --accent: #4ea6ec;
    --button: #5aa9ea;
    --text-light: #ffffff;
    --text-muted: #b9b9bc;
    --search-text: #c3c7cc;
    --logo-box: #d9d9d9;
    --arrow: #5b5b5e;
  }
  * { box-sizing: border-box; margin: 0; padding: 0; }
  html, body { width: 1200px; height: 686px; overflow: hidden; }
  body {
    background: var(--strip-bg);
    font-family: "Josefin Sans", sans-serif;
    color: var(--text-light);
  }
  .site { width: 1200px; height: 686px; display: flex; flex-direction: column; }

  /* Header */
  .site-header {
    height: 70px; flex: none;
    background: var(--header-bg);
    display: flex;
    align-items: center;
    padding: 0 32px 0 22px;
  }
  .brand { display: flex; align-items: center; gap: 8px; margin-right: 22px; }
  .brand-mark { width: 16px; height: 16px; background: var(--logo-box); }
  .brand-name {
    font-size: 13px; font-weight: 600; letter-spacing: .06em;
    text-transform: uppercase; color: var(--text-light); line-height: 1;
  }
  .main-nav { display: flex; gap: 17px; flex: 1; }
  .main-nav a {
    color: var(--text-light); text-decoration: none; font-weight: 600;
    font-size: 13px; text-transform: uppercase; letter-spacing: .02em;
  }
  .main-nav a.is-current { color: var(--accent); }
  .header-actions { display: flex; gap: 16px; }
  .btn {
    width: 70px; height: 30px; border-radius: 3px;
    background: var(--button); color: var(--text-light);
    font-size: 12px; font-weight: 700; text-transform: uppercase;
    display: flex; align-items: center; justify-content: center; text-decoration: none;
  }

  /* Hero */
  .hero {
    position: relative; height: 406px; flex: none;
    background:
      radial-gradient(ellipse 60% 40% at 50% 78%, rgba(180,200,150,.35), transparent 70%),
      linear-gradient(180deg,
        #5f9fd6 0%, #8fbde2 10%, #b7d3e6 15%, #2f6f95 19%, #3d7d9c 23%,
        #566f52 27%, #2f5a2c 38%, #3f6e34 52%, #4f8a3a 64%, #68a545 76%, #79b24c 90%, #6aa043 100%);
  }
  .property-search {
    position: absolute; left: 50%; top: 50%; transform: translate(-50%, -50%);
    width: 410px; height: 48px; background: #fff; border-radius: 4px;
    box-shadow: 0 2px 10px rgba(0,0,0,.35);
    display: flex; align-items: center; padding: 0 18px; gap: 16px;
  }
  .property-search span {
    flex: 1; text-align: center; color: var(--search-text);
    font-weight: 700; font-size: 15px; letter-spacing: .04em; text-transform: uppercase;
    padding-right: 30px;
  }

  /* Listings strip */
  .listings {
    flex: 1; background: var(--strip-bg);
    display: flex; align-items: center; padding: 0 12px;
  }
  .carousel-arrow { width: 26px; display: flex; justify-content: center; }
  .listing-track { flex: 1; display: flex; gap: 24px; padding: 0 14px; }
  .listing-card { display: flex; gap: 16px; width: 358px; }
  .listing-photo { width: 156px; height: 160px; flex: none; }
  .listing-photo.dusk { background: linear-gradient(180deg, #3d4550, #6a6258 60%, #4a4038); }
  .listing-photo.pool { background: linear-gradient(180deg, #1c3c72, #c98a3c 55%, #2aa6c8); }
  .listing-photo.evening { background: linear-gradient(180deg, #6b8fb8, #8c7a5e 55%, #2d9fc2); }
  .listing-info { padding-top: 6px; }
  .listing-status { color: var(--accent); font-size: 14px; font-weight: 700; text-transform: uppercase; }
  .listing-price { font-size: 16px; font-weight: 600; margin-top: 14px; text-transform: uppercase; }
  .listing-place {
    display: flex; align-items: center; gap: 5px; margin-top: 14px;
    font-size: 9px; color: var(--text-muted); text-transform: uppercase;
  }
  .listing-agent { display: flex; align-items: center; gap: 10px; margin-top: 22px; }
  .agent-photo { width: 30px; height: 30px; border-radius: 50%; background: #6e5e52; flex: none; }
  .agent-contact { font-size: 9px; line-height: 1.6; color: var(--text-muted); text-transform: uppercase; }
</style>
</head>
<body>
<div class="site">
  <header class="site-header">
    <div class="brand">
      <span class="brand-mark"></span>
      <span class="brand-name">Marlow on the Shore</span>
    </div>
    <nav class="main-nav">
      <a class="is-current" href="#">Welcome</a>
      <a href="#">Featured Listings</a>
      <a href="#">Previously Sold</a>
      <a href="#">Team</a>
      <a href="#">Videos</a>
      <a href="#">Blog</a>
      <a href="#">Explore O.C.</a>
      <a href="#">Contact</a>
    </nav>
    <div class="header-actions">
      <a class="btn" href="#">Sell</a>
      <a class="btn" href="#">Buy</a>
    </div>
  </header>

  <section class="hero" role="img" aria-label="Oceanfront resort with palm trees, a white pergola and green lawns overlooking the Pacific coast">
    <div class="property-search">
      <svg width="20" height="20" viewBox="0 0 20 20" aria-hidden="true">
        <circle cx="12" cy="8" r="5.5" fill="none" stroke="#4ea6ec" stroke-width="2.4"/>
        <line x1="8" y1="12" x2="2.5" y2="17.5" stroke="#4ea6ec" stroke-width="3" stroke-linecap="round"/>
      </svg>
      <span>Property Search</span>
    </div>
  </section>

  <section class="listings">
    <div class="carousel-arrow">
      <svg width="14" height="28" viewBox="0 0 14 28" aria-hidden="true"><polyline points="11,3 3,14 11,25" fill="none" stroke="#5b5b5e" stroke-width="4"/></svg>
    </div>
    <div class="listing-track">
      <article class="listing-card">
        <div class="listing-photo dusk" role="img" aria-label="Stone mansion at dusk"></div>
        <div class="listing-info">
          <div class="listing-status">For Sale</div>
          <div class="listing-price">$ 3 Million</div>
          <div class="listing-place">
            <svg width="8" height="11" viewBox="0 0 8 11" aria-hidden="true"><path d="M4 0a4 4 0 0 1 4 4c0 3-4 7-4 7S0 7 0 4a4 4 0 0 1 4-4z" fill="#4ea6ec"/><circle cx="4" cy="4" r="1.4" fill="#3a3a3c"/></svg>
            Beverly Hills, California
          </div>
          <div class="listing-agent">
            <div class="agent-photo" role="img" aria-label="Agent portrait"></div>
            <div class="agent-contact">Contact Ellis<br>Phone 1.800.555.0142</div>
          </div>
        </div>
      </article>
      <article class="listing-card">
        <div class="listing-photo pool" role="img" aria-label="Lit villa with pool at night"></div>
        <div class="listing-info">
          <div class="listing-status">For Sale</div>
          <div class="listing-price">$ 1.8 Million</div>
          <div class="listing-place">
            <svg width="8" height="11" viewBox="0 0 8 11" aria-hidden="true"><path d="M4 0a4 4 0 0 1 4 4c0 3-4 7-4 7S0 7 0 4a4 4 0 0 1 4-4z" fill="#4ea6ec"/><circle cx="4" cy="4" r="1.4" fill="#3a3a3c"/></svg>
            Beverly Hills, California
          </div>
          <div class="listing-agent">
            <div class="agent-photo" role="img" aria-label="Agent portrait"></div>
            <div class="agent-contact">Contact Ellis<br>Phone 1.800.555.0142</div>
          </div>
        </div>
      </article>
      <article class="listing-card">
        <div class="listing-photo evening" role="img" aria-label="Modern home with pool in the evening"></div>
        <div class="listing-info">
          <div class="listing-status">For Sale</div>
          <div class="listing-price">$ 900,000</div>
          <div class="listing-place">
            <svg width="8" height="11" viewBox="0 0 8 11" aria-hidden="true"><path d="M4 0a4 4 0 0 1 4 4c0 3-4 7-4 7S0 7 0 4a4 4 0 0 1 4-4z" fill="#4ea6ec"/><circle cx="4" cy="4" r="1.4" fill="#3a3a3c"/></svg>
            Beverly Hills, California
          </div>
          <div class="listing-agent">
            <div class="agent-photo" role="img" aria-label="Agent portrait"></div>
            <div class="agent-contact">Contact Ellis<br>Phone 1.800.555.0142</div>
          </div>
        </div>
      </article>
    </div>
    <div class="carousel-arrow">
      <svg width="14" height="28" viewBox="0 0 14 28" aria-hidden="true"><polyline points="3,3 11,14 3,25" fill="none" stroke="#5b5b5e" stroke-width="4"/></svg>
    </div>
  </section>
</div>
</body>
</html>
```